I need a book cover for my book titled Sunny Porch! The subtitle is Quiet Orchard Days and the the author is Marisol Dunleavy. I want the attached photo included on the cover, plus the words "I never met a chicken wing I didn't like!" The book size is 5.06 x 7.81 in. and is 146 pages. For the color scheme, I like a chocolate brown cover with aqua blue letters. (Please note that you don't have to use these colors. Feel free to use this color scheme or whatever you colors you like!)

• Please include my photo for the back cover, along with this text:

Sunny Porch! I was tired of being tired! I was tired of acid reflux, body stiffness, and being overweight. To make matters worse, I suffered from back pain, constipation, leg pain, and lack of sleep. If you are tired of looking to medical test for your answers, this is the book for you. The key was the day I decided to make “me” a priority by being #1 on my “to-do” list.

Our healthcare system seems to be more concerned about treating illness than they are about preventing it; which is why we have so many problems with our health and wellness. That’s why I’m going to give you insights into nutrition, health care, and the pharmaceutical industry.

I’m also going to give you some insights into exercise, supplements, detoxing and essential oils; as well as what goes into your grocery cart and the foods you feed your family.

Because you’re reading this I know you’re ready to live your best life, Sunny Porch! is for you.

Here’s to a healthy you!

Here's a brief bio about the author for the back cover:

Marisol lives in Chicago with her husband, Dr. Wendell, and has three adult children. She is probably one of the most private people you will meet – BUT HAD to tell her story!

```html
<!DOCTYPE html>
<html lang="en">
<head>
<meta charset="utf-8">
<title>Sunny Porch! – Book Cover Layout</title>
<link href="https://fonts.googleapis.com/css2?family=Nunito+Sans:wght@400;600;700;800;900&family=Source+Sans+3:wght@600;700&display=swap" rel="stylesheet">
<style>
  :root {
    --canvas: #ffffff;
    --choc-dark: #5e3300;
    --choc: #7a4508;
    --choc-light: #8a530f;
    --aqua: #2fb9e6;
    --aqua-deep: #0a9fd0;
    --aqua-text: #21c4ea;
    --white: #ffffff;
    --label: #5a5a5a;
    --photo-portrait: #6b4a2a;
    --photo-food: #c8c2bc;
  }
  * { margin: 0; padding: 0; box-sizing: border-box; }
  html, body { width: 1200px; height: 1000px; overflow: hidden; background: var(--canvas); }
  .canvas { position: relative; width: 1200px; height: 1000px; font-family: "Nunito Sans", sans-serif; }

  .floor-shadow {
    position: absolute; left: 60px; top: 745px; width: 1090px; height: 40px;
    background: radial-gradient(ellipse at center, rgba(0,0,0,0.10) 0%, rgba(0,0,0,0) 70%);
  }

  .panel { position: absolute; top: 176px; height: 582px; overflow: hidden;
    background: radial-gradient(ellipse at 50% 10%, var(--choc-light) 0%, var(--choc) 45%, var(--choc-dark) 100%); }
  .panel-back { left: 149px; width: 378px; }
  .panel-spine { left: 567px; width: 65px; background: var(--choc); }
  .panel-front { left: 673px; width: 378px; }

  .aqua-band { position: absolute; left: 0; right: 0; bottom: 0;
    background: linear-gradient(180deg, var(--aqua) 0%, var(--aqua-deep) 100%); }
  .panel-back .aqua-band { top: 478px; clip-path: polygon(0 16px, 100% 0, 100% 100%, 0 100%); }
  .panel-spine .aqua-band { top: 186px; clip-path: polygon(0 0, 100% 18px, 100% 100%, 0 100%); }
  .panel-front .aqua-band { top: 342px; clip-path: polygon(0 0, 100% 80px, 100% 100%, 0 100%); }

  /* back cover */
  .author-photo { position: absolute; left: 138px; top: 40px; width: 122px; height: 186px;
    background: linear-gradient(180deg, #3b2a1a 0%, var(--photo-portrait) 50%, #2b1d10 100%); }
  .back-blurb { position: absolute; left: 50px; top: 244px; width: 280px; text-align: center;
    color: var(--aqua-text); font-size: 7.6px; line-height: 10.4px; }
  .back-blurb p { margin-bottom: 7px; }
  .author-bio { position: absolute; left: 46px; top: 522px; width: 286px; text-align: center;
    color: var(--white); font-size: 7.6px; line-height: 10.4px; }

  /* spine */
  .spine-text { position: absolute; writing-mode: vertical-rl; transform: rotate(180deg);
    color: var(--white); white-space: nowrap; }
  .spine-author { left: 25px; top: 26px; height: 144px; font-size: 13px; text-align: center; }
  .spine-subtitle { left: 25px; top: 220px; height: 132px; font-size: 13.5px; text-align: center; }
  .spine-title { left: 16px; top: 378px; height: 170px; font-size: 29px; font-weight: 800; text-align: center; }

  /* front cover */
  .title-banner { position: absolute; left: 52px; top: 72px; width: 276px; height: 78px;
    background: linear-gradient(180deg, var(--aqua) 0%, var(--aqua-deep) 100%);
    clip-path: polygon(0 10px, 100% 0, 98% 100%, 2% 100%);
    box-shadow: 0 3px 6px rgba(0,0,0,0.3); }
  .title-main { position: absolute; left: 52px; top: 80px; width: 276px; text-align: center;
    color: var(--white); font-size: 36px; font-weight: 800; line-height: 40px; }
  .title-sub { position: absolute; left: 52px; top: 123px; width: 276px; text-align: center;
    color: var(--white); font-size: 16.5px; line-height: 20px; }
  .front-author { position: absolute; left: 0; width: 378px; top: 172px; text-align: center;
    color: var(--aqua-text); font-size: 17px; font-weight: 600; }
  .food-photo { position: absolute; left: 36px; top: 246px; width: 312px; height: 210px;
    border-radius: 18px;
    background: radial-gradient(ellipse at 60% 60%, #a6341a 0%, #c77a56 35%, var(--photo-food) 65%, rgba(200,194,188,0) 100%); }
  .tagline { position: absolute; left: 0; width: 378px; top: 484px; text-align: center;
    color: var(--white); font-size: 21px; font-weight: 800; line-height: 25px; }

  .panel-label { position: absolute; top: 803px; font-family: "Source Sans 3", sans-serif;
    font-weight: 700; font-size: 23px; color: var(--label); text-align: center; }
  .label-back { left: 286px; width: 100px; }
  .label-spine { left: 550px; width: 100px; }
  .label-front { left: 805px; width: 100px; top: 806px; }
</style>
</head>
<body>
<div class="canvas">
  <div class="floor-shadow"></div>

  <section class="panel panel-back">
    <div class="aqua-band"></div>
    <div class="author-photo" role="img" aria-label="Portrait photograph of the author"></div>
    <div class="back-blurb">
      <p>Sunny Porch! I was tired of being tired! I was tired of acid reflux, body stiffness, and being overweight. To make matters worse, I suffered from back pain, constipation, leg pain, and lack of sleep. If you are tired of looking to medical test for your answers, this is the book for you. The key was the day I decided to make “me” a priority by being #1 on my “to-do” list.</p>
      <p>Our healthcare system seems to be more concerned about treating illness than they are about preventing it; which is why we have so many problems with our health and wellness. That’s why I’m going to give you insights into nutrition, health care, and the pharmaceutical industry.</p>
      <p>I’m also going to give you some insights into exercise, supplements, detoxing and essential oils; as well as what goes into your grocery cart and the foods you feed your family.</p>
      <p>Because you’re reading this I know you’re ready to live your best life, Sunny Porch! is for you.</p>
      <p>Here’s to a healthy you!</p>
    </div>
    <p class="author-bio">Marisol lives in Chicago with her husband, Dr. Wendell, and has three adult children. She is probably one of the most private people you will meet – BUT HAD to tell her story!</p>
  </section>

  <section class="panel panel-spine">
    <div class="aqua-band"></div>
    <span class="spine-text spine-author">By Marisol Dunleavy</span>
    <span class="spine-text spine-subtitle">Quiet Orchard Days</span>
    <span class="spine-text spine-title">Sunny Porch!</span>
  </section>

  <section class="panel panel-front">
    <div class="aqua-band"></div>
    <div class="title-banner"></div>
    <h1 class="title-main">Sunny Porch!</h1>
    <p class="title-sub">Quiet Orchard Days</p>
    <p class="front-author">By Marisol Dunleavy</p>
    <div class="food-photo" role="img" aria-label="Photograph of a tray of glazed chicken wings with celery, carrots and dip, tray rim marked with warning labels"></div>
    <p class="tagline">I never met a chicken wing<br>I didn't like!</p>
  </section>

  <div class="panel-label label-back">Back</div>
  <div class="panel-label label-spine">Side</div>
  <div class="panel-label label-front">Front</div>
</div>
</body>
</html>
```